Simple, elegant, business card design required

Hi designers,I am looking for a simple yet elegant business card design.

Please make use of my logo (attached); you are free to tweak the logo should you wish to do so.

Our business is involved in many different fields - almost all of them involved in some form of "design", so that's really one of the key things I want to portray. I do not wish to specify which field of design, exactly.

I prefer white on black (or just monochromatic), but if you have a different, creative idea, I am open to that too.

You can use artsy photographs provided that you have the license to use those. Please feel free to ask me any questions.

Target Market(s)

High-end customers looking for design consultancy

Industry/Entity Type

Business

Contact Information for Business Card

Name: Gareth Pellwinter
Position: Creative Director
Mobile: +150963218745
Address: Morrow Lane, Stratford upon Avon, Warwickshire CV37 2JT
Website: corvastudio.com (not launched yet)

Requirements
Must have
• Design layout must be clean, original, and text must be readable when printed.
Should not have
• ~ No business card templates please. Anyone using this will be reported.
• ~ Please don't spam entries.

```html
<!DOCTYPE html>
<html lang="en">
<head>
<meta charset="utf-8">
<title>Corva Studio — Business Card</title>
<link rel="stylesheet" href="https://fonts.googleapis.com/css2?family=Jost:wght@400;500;700&display=swap">
<style>
  :root {
    --canvas-bg: #e4e2df;
    --ink: #0f0f0f;
    --charcoal: #2b2b2b;
    --charcoal-deep: #131313;
    --paper: #f4f4f4;
    --paper-shade: #dcdcdc;
    --text-dark: #1a1a1a;
    --text-soft: #3a3a3a;
    --white: #ffffff;
  }
  * { margin: 0; padding: 0; box-sizing: border-box; }
  html, body {
    width: 1200px;
    height: 900px;
    overflow: hidden;
    background: var(--canvas-bg);
    font-family: "Jost", "Futura", sans-serif;
  }
  .canvas {
    width: 1200px;
    height: 900px;
    display: flex;
    flex-direction: column;
    align-items: center;
    justify-content: center;
    gap: 40px;
  }
  .card {
    width: 700px;
    height: 400px;
    position: relative;
    overflow: hidden;
    box-shadow: 0 10px 30px rgba(0,0,0,0.18);
  }

  /* Back of card */
  .card--back {
    background: var(--charcoal);
    display: flex;
  }
  .card--back .brand-strip {
    width: 190px;
    height: 100%;
    background: var(--ink);
    display: flex;
    align-items: center;
    justify-content: center;
  }
  .brand-dot {
    width: 44px;
    height: 44px;
    border-radius: 50%;
    background: var(--white);
    flex: none;
  }
  .card--back .brand-name {
    flex: 1;
    display: flex;
    align-items: center;
    padding-left: 60px;
    font-size: 40px;
    font-weight: 400;
    letter-spacing: 0.32em;
    color: var(--charcoal-deep);
    text-transform: uppercase;
    white-space: nowrap;
  }

  /* Front of card */
  .card--front {
    background: linear-gradient(160deg, var(--paper) 0%, var(--paper) 45%, var(--paper-shade) 100%);
  }
  .front-block {
    position: absolute;
    top: 0;
    left: 0;
    width: 300px;
    height: 190px;
    background: var(--ink);
    display: flex;
    align-items: center;
    justify-content: center;
    gap: 14px;
  }
  .front-block .brand-dot { width: 18px; height: 18px; }
  .front-block .brand-name {
    color: var(--white);
    font-size: 22px;
    font-weight: 400;
    letter-spacing: 0.28em;
    text-transform: uppercase;
    white-space: nowrap;
  }
  .contact {
    position: absolute;
    right: 56px;
    top: 150px;
    text-align: right;
    text-transform: uppercase;
    color: var(--text-soft);
    font-size: 13px;
    letter-spacing: 0.2em;
    line-height: 1.75;
    white-space: nowrap;
  }
  .contact .person-name {
    font-weight: 700;
    font-size: 15px;
    color: var(--text-dark);
    letter-spacing: 0.24em;
  }
  .contact .person-title { margin-bottom: 22px; }
  .contact .line {
    display: flex;
    justify-content: flex-end;
    align-items: center;
    gap: 10px;
  }
  .contact .icon { width: 14px; height: 14px; flex: none; }
</style>
</head>
<body>
<main class="canvas">
  <section class="card card--back" aria-label="Card back">
    <div class="brand-strip"><span class="brand-dot"></span></div>
    <div class="brand-name">Corva Studio</div>
  </section>

  <section class="card card--front" aria-label="Card front">
    <div class="front-block">
      <span class="brand-dot"></span>
      <span class="brand-name">Corva Studio</span>
    </div>
    <div class="contact">
      <p class="person-name">Gareth Pellwinter</p>
      <p class="person-title">Creative Director</p>
      <p>Morrow Lane</p>
      <p>Ashcombe Vale</p>
      <p>Dunmere DM12 2JT</p>
      <p class="line">+150963218745
        <svg class="icon" viewBox="0 0 14 14" aria-hidden="true">
          <rect x="3.5" y="1" width="7" height="12" rx="1.2" fill="none" stroke="#1a1a1a" stroke-width="1.2"/>
          <line x1="6" y1="11" x2="8" y2="11" stroke="#1a1a1a" stroke-width="1"/>
        </svg>
      </p>
      <p class="line">Website: corvastudio.com
        <svg class="icon" viewBox="0 0 14 14" aria-hidden="true">
          <circle cx="7" cy="7" r="5.8" fill="none" stroke="#1a1a1a" stroke-width="1.2"/>
          <ellipse cx="7" cy="7" rx="2.5" ry="5.8" fill="none" stroke="#1a1a1a" stroke-width="1"/>
          <line x1="1.2" y1="7" x2="12.8" y2="7" stroke="#1a1a1a" stroke-width="1"/>
        </svg>
      </p>
    </div>
  </section>
</main>
</body>
</html>
```